Business card for Chiropractic clinics needs reworked / redesigned

The business card in attachment was designed 10 years ago. It is in need of an update.
We have 2 clinics:
VELDHOVE KLINIEK & VELDHOVE KLINIEK NOORD
Only one address needs to be on the card for doctors that only work in one clinic and two addresses need to be on the card for the doctors that work in both clinics.

Target Market(s)

patients/referrers

Industry/Entity Type

Medical

Contact Information for Business Card

Logo (in full or zoomed-in)
Clinic Name
Doctor name and title
clinic address, website, tel, email

Font styles to use
Sans Serif

Colors

Designer to choose colors to be used in the design.

Requirements
Must have
• Good contrast/readability
• We like modern minimalistic designs
• The Bcard needs to project our very high standard of proficiency/professionalism
Should not have
• Not curly
• Not to much colours

```html
<!DOCTYPE html>
<html lang="nl">
<head>
<meta charset="utf-8">
<title>Veldhove Kliniek – visitekaartje</title>
<link rel="stylesheet" href="https://fonts.googleapis.com/css2?family=Oswald:wght@500;600&family=Roboto:wght@300;400&display=swap">
<style>
  :root {
    --bg: #e9ebea;
    --card-green: #124a3a;
    --card-green-soft: #1a5a47;
    --ink: #ffffff;
    --shadow: rgba(0, 0, 0, 0.18);
  }
  * { box-sizing: border-box; margin: 0; padding: 0; }
  html, body { width: 1200px; height: 804px; overflow: hidden; }
  body {
    background: var(--bg);
    font-family: "Roboto", Arial, sans-serif;
    color: var(--ink);
    display: flex;
    align-items: center;
    justify-content: center;
    gap: 40px;
  }
  .card {
    position: relative;
    width: 560px;
    height: 320px;
    background: var(--card-green);
    box-shadow: 0 10px 30px var(--shadow);
    overflow: hidden;
  }

  /* Front */
  .card-front .symbol-area {
    position: absolute;
    left: 70px;
    top: 80px;
    width: 200px;
    height: 240px;
    background: linear-gradient(160deg, var(--card-green-soft), var(--card-green));
  }
  .card-front .brand {
    position: absolute;
    right: 40px;
    top: 92px;
    text-align: right;
    font-family: "Oswald", "Arial Narrow", sans-serif;
    font-weight: 600;
    font-size: 32px;
    letter-spacing: 0.03em;
    line-height: 1.1;
  }
  .card-front .brand span { display: block; }

  /* Back */
  .card-back .person {
    position: absolute;
    left: 32px;
    bottom: 40px;
    width: 250px;
    line-height: 1.3;
  }
  .card-back .person-name { font-size: 20px; font-weight: 400; }
  .card-back .person-title,
  .card-back .person-number { font-size: 15px; font-weight: 300; letter-spacing: 0.04em; }

  .card-back .divider {
    position: absolute;
    left: 296px;
    top: 30px;
    width: 2px;
    height: 260px;
    background: var(--ink);
  }
  .card-back .clinics {
    position: absolute;
    left: 314px;
    right: 26px;
    top: 28px;
    bottom: 28px;
    display: flex;
    flex-direction: column;
    justify-content: space-between;
    text-align: right;
  }
  .clinic-name {
    font-family: "Oswald", "Arial Narrow", sans-serif;
    font-size: 17px;
    font-weight: 600;
    letter-spacing: 0.03em;
    line-height: 1.2;
    margin-bottom: 6px;
    white-space: nowrap;
  }
  .clinic-details {
    font-style: normal;
    font-size: 12.5px;
    font-weight: 300;
    line-height: 1.5;
  }
</style>
</head>
<body>

  <section class="card card-front" aria-label="Voorzijde visitekaartje">
    <div class="symbol-area" role="img" aria-label="Beeldmerk van de kliniek: gestileerde wervelkolom"></div>
    <div class="brand">
      <span>VELDHOVE</span>
      <span>KLINIEK</span>
    </div>
  </section>

  <section class="card card-back" aria-label="Achterzijde visitekaartje">
    <div class="person">
      <p class="person-name">Pieter VERSCHAEVE D.C.</p>
      <p class="person-title">CHIROPRACTOR</p>
      <p class="person-number">0.12345.67.000</p>
    </div>

    <div class="divider" aria-hidden="true"></div>

    <div class="clinics">
      <div class="clinic">
        <p class="clinic-name">VELDHOVE KLINIEK</p>
        <address class="clinic-details">
          Lindenlaan 48<br>
          +32 (0) 9 000.14.20<br>
          info@veldhovekliniek.be<br>
          www.veldhovekliniek.be
        </address>
      </div>
      <div class="clinic">
        <p class="clinic-name">VELDHOVE KLINIEK NOORD</p>
        <address class="clinic-details">
          Molenstraat 17<br>
          +32 (0) 9 000.38.55<br>
          www.veldhovenoord.be
        </address>
      </div>
    </div>
  </section>

</body>
</html>
```